Brightpath Holdings Business Card

Create a two sided, high gloss, quality business card for Brightpath Holdings.

Target Market(s)

People wanting to purchase, scale, and sell businesses.

Industry/Entity Type

Entrepreneurs

Contact Information for Business Card

One line: Dana Corwell, CPA, CMA Another line: Entrepreneur & Investor Another line: Business Ownership Transition Expert Another line: Multi-State Licensed Real Estate Broker Phone 954-BRTPATH (278-7284) Email Dana@Brightpath Holdings.com Website www.Brightpath.com

Requirements
Must have
• Black Card, logo on one side, all other information on the other side including a small logo.
Nice to have
• Possibly add a tagline "Helping entrepreneurs live a life they don't need a vacation from"
Should not have
• There will not be a mailing address on these cards.

```html
<!DOCTYPE html>
<html lang="en">
<head>
<meta charset="UTF-8">
<title>Brightpath Holdings Business Card</title>
<link href="https://fonts.googleapis.com/css2?family=Montserrat:wght@300;400;600;700&display=swap" rel="stylesheet">
<style>
  :root {
    --page-bg: #2b2621;
    --card-black: #0f0d0e;
    --card-sheen: #2a2829;
    --gold: #d6a83e;
    --text-white: #e9e6e1;
  }
  * { margin: 0; padding: 0; box-sizing: border-box; }
  html, body {
    width: 1200px;
    height: 1014px;
    overflow: hidden;
    background: var(--page-bg);
    font-family: 'Montserrat', sans-serif;
  }
  .canvas {
    width: 1200px;
    height: 1014px;
    display: flex;
    flex-direction: column;
    align-items: center;
    justify-content: center;
    gap: 24px;
  }
  .card {
    position: relative;
    width: 840px;
    height: 480px;
    border-radius: 6px;
    background: linear-gradient(125deg, var(--card-sheen) 0%, var(--card-black) 38%, var(--card-black) 70%, #1c1a1b 100%);
    box-shadow: 0 14px 30px rgba(0,0,0,0.5);
    overflow: hidden;
  }

  /* Info side */
  .card-info .identity {
    position: absolute;
    left: 70px;
    top: 70px;
  }
  .card-info .name {
    color: var(--gold);
    font-weight: 600;
    font-size: 34px;
    letter-spacing: 0.5px;
    margin-bottom: 10px;
  }
  .card-info .title-line {
    color: var(--text-white);
    font-weight: 300;
    font-size: 24px;
    line-height: 36px;
  }
  .card-info .contact {
    position: absolute;
    left: 300px;
    top: 300px;
    list-style: none;
  }
  .card-info .contact li {
    display: flex;
    align-items: center;
    gap: 14px;
    color: var(--text-white);
    font-weight: 300;
    font-size: 23px;
    line-height: 40px;
  }
  .card-info .contact svg { width: 22px; height: 22px; flex: none; }

  .small-brand {
    position: absolute;
    right: 56px;
    top: 80px;
    display: flex;
    align-items: center;
    gap: 8px;
  }
  .small-brand .brand-mark { width: 14px; height: 14px; }
  .small-brand .brand-name { font-size: 16px; font-weight: 700; letter-spacing: 0.3px; }

  /* Logo side */
  .card-logo {
    display: flex;
    align-items: center;
    justify-content: center;
  }
  .brand {
    display: flex;
    align-items: center;
    gap: 20px;
  }
  .brand-mark {
    width: 40px;
    height: 40px;
    border-radius: 50%;
    background: var(--gold);
  }
  .brand-name {
    color: var(--gold);
    font-weight: 700;
    font-size: 58px;
    letter-spacing: 0.5px;
  }
</style>
</head>
<body>
<main class="canvas">
  <section class="card card-info" aria-label="Business card, contact side">
    <div class="brand small-brand">
      <span class="brand-mark" aria-hidden="true"></span>
      <span class="brand-name">Brightpath Holdings</span>
    </div>
    <div class="identity">
      <h1 class="name">Dana Corwell</h1>
      <p class="title-line">CPA, CMA, Entrepreneur, Investor</p>
      <p class="title-line">Business Ownership Transition Expert</p>
      <p class="title-line">Multi-State Licensed Real Estate Broker</p>
    </div>
    <ul class="contact">
      <li>
        <svg viewBox="0 0 24 24" aria-hidden="true"><path fill="#d6a83e" d="M6.6 10.8a15.1 15.1 0 0 0 6.6 6.6l2.2-2.2c.3-.3.7-.4 1-.2 1.1.4 2.3.6 3.6.6.6 0 1 .4 1 1V20c0 .6-.4 1-1 1A17 17 0 0 1 3 4c0-.6.4-1 1-1h3.5c.6 0 1 .4 1 1 0 1.3.2 2.5.6 3.6.1.3 0 .7-.2 1z"/></svg>
        <span>954-BRTPATH (278-7284)</span>
      </li>
      <li>
        <svg viewBox="0 0 24 24" aria-hidden="true"><rect x="2" y="5" width="20" height="14" rx="1.5" fill="#d6a83e"/><path d="M3 6l9 7 9-7" fill="none" stroke="#0f0d0e" stroke-width="1.6"/></svg>
        <span>Dana@Brightpath Holdings.com</span>
      </li>
      <li>
        <svg viewBox="0 0 24 24" aria-hidden="true"><circle cx="12" cy="12" r="10" fill="#d6a83e"/><g fill="none" stroke="#0f0d0e" stroke-width="1.3"><ellipse cx="12" cy="12" rx="4.2" ry="10"/><path d="M2 12h20M4 7h16M4 17h16"/></g></svg>
        <span>www.Brightpath.com</span>
      </li>
    </ul>
  </section>

  <section class="card card-logo" aria-label="Business card, logo side">
    <div class="brand">
      <span class="brand-mark" aria-hidden="true"></span>
      <span class="brand-name">Brightpath Holdings</span>
    </div>
  </section>
</main>
</body>
</html>
```